Medical program Vora produce by HALVOCARE

I need a business card of the program to give to the customer to get the general information to contact the clinic. I need a bilingual card French and English you will see the logo.
That's a program that the Clinic Halvocare offers. https://medicalvora.ca
Program: Vora Medical Program
Slogan: SHED WEIGHT - THRIVE - LIVE / Be thin - Exist - Live
The clinic that offers the program: Halvocare
Website: https://medicalvora.ca
---
Medical team / Medical team
email: doc@halvocare.ca
phone: 514 555-0148
Information
email: vora@halvocare.ca
phone: 514 555-0172 ext 3
Every person that needs to lose weight
Health clinic for obese person
All the information in the description
- Look clean - Expensive clinic / Need to be bilingual
- Recto verso for french and english

```html
<!DOCTYPE html>
<html lang="en">
<head>
<meta charset="utf-8">
<title>Halvocare – Vora business cards</title>
<link href="https://fonts.googleapis.com/css2?family=Poppins:wght@300;400;500;600;700&display=swap" rel="stylesheet">
<style>
  :root {
    --backdrop: #737373;
    --card: #ffffff;
    --red: #db2d38;
    --ink: #08090b;
    --teal: #13a89e;
    --blue: #0083cc;
    --text: #3a3a3a;
  }
  * { box-sizing: border-box; margin: 0; padding: 0; }
  html, body { width: 1200px; height: 1200px; overflow: hidden; }
  body {
    background: var(--backdrop);
    font-family: "Poppins", sans-serif;
    position: relative;
  }
  .card {
    position: absolute;
    left: 281px;
    width: 639px;
    height: 366px;
    background: var(--card);
    border-radius: 24px;
    overflow: hidden;
  }
  .card--clinic { top: 195px; }
  .card--program { top: 639px; }

  /* clinic brand */
  .brand-mark {
    position: absolute;
    left: 48px; top: 42px;
    width: 96px; height: 96px;
    background: var(--red);
  }
  .brand-name {
    position: absolute;
    left: 152px; top: 70px;
    font-size: 38px;
    font-weight: 700;
    line-height: 1;
    color: var(--ink);
    letter-spacing: 0.5px;
    white-space: nowrap;
  }
  .brand-tagline {
    position: absolute;
    left: 175px; top: 116px;
    font-size: 12px;
    font-weight: 400;
    letter-spacing: 1px;
    color: var(--red);
    white-space: nowrap;
  }

  /* program brand */
  .program-mark {
    position: absolute;
    left: 48px; top: 94px;
    width: 26px; height: 26px;
    border-radius: 50%;
    background: var(--teal);
  }
  .program-name {
    position: absolute;
    left: 84px; top: 64px;
    font-size: 72px;
    font-weight: 300;
    line-height: 1;
    color: var(--teal);
    white-space: nowrap;
  }
  .program-tagline {
    position: absolute;
    left: 86px; top: 134px;
    font-size: 8px;
    font-weight: 500;
    letter-spacing: 1.2px;
    color: var(--blue);
    white-space: nowrap;
  }

  /* contact block */
  .contact {
    position: absolute;
    right: 48px;
    top: 246px;
    text-align: right;
    list-style: none;
  }
  .contact li {
    display: flex;
    align-items: center;
    justify-content: flex-end;
    gap: 8px;
    font-size: 16.5px;
    line-height: 21px;
    color: var(--text);
    letter-spacing: 0.6px;
    white-space: nowrap;
  }
  .contact .phone { font-weight: 600; }
  .contact .email { font-weight: 300; }
  .contact svg { width: 11px; height: 11px; flex: none; }

  /* bottom band */
  .band {
    position: absolute;
    left: 0; bottom: 0;
    width: 639px; height: 46px;
  }
  .band svg { position: absolute; inset: 0; }
  .band-url {
    position: absolute;
    left: 0; width: 642px;
    top: 0; height: 46px;
    line-height: 46px;
    text-align: center;
    color: #ffffff;
    font-size: 16px;
    font-weight: 600;
    letter-spacing: 3.6px;
  }
</style>
</head>
<body>

  <section class="card card--clinic" aria-label="Halvocare card">
    <div class="brand-mark"></div>
    <div class="brand-name">HALVOCARE</div>
    <div class="brand-tagline">SHED WEIGHT - THRIVE - LIVE</div>

    <ul class="contact">
      <li class="phone">514 555-0148
        <svg viewBox="0 0 24 24"><path fill="var(--red)" d="M6.6 10.8a15.1 15.1 0 0 0 6.6 6.6l2.2-2.2c.3-.3.7-.4 1-.2 1.1.4 2.3.6 3.6.6.6 0 1 .4 1 1V20c0 .6-.4 1-1 1A17 17 0 0 1 3 4c0-.6.4-1 1-1h3.5c.6 0 1 .4 1 1 0 1.3.2 2.5.6 3.6.1.3 0 .7-.2 1z"/></svg>
      </li>
      <li class="email">doc@halvocare.ca
        <svg viewBox="0 0 24 24"><rect x="1" y="4" width="22" height="16" fill="var(--red)"/><path d="M2 5l10 8 10-8" stroke="#fff" stroke-width="2" fill="none"/></svg>
      </li>
    </ul>

    <div class="band">
      <svg viewBox="0 0 639 46" preserveAspectRatio="none">
        <polygon points="0,0 477,0 527,46 0,46" fill="var(--red)"/>
        <polygon points="490,0 639,0 639,46 541,46" fill="var(--ink)"/>
      </svg>
      <div class="band-url">MEDICALVORA.CA</div>
    </div>
  </section>

  <section class="card card--program" aria-label="Vora program card">
    <div class="program-mark"></div>
    <div class="program-name">Vora</div>
    <div class="program-tagline">MINCIR-RAYONNER-VIVRE</div>

    <ul class="contact">
      <li class="phone">514 555-0172 ext 3
        <svg viewBox="0 0 24 24"><path fill="var(--blue)" d="M6.6 10.8a15.1 15.1 0 0 0 6.6 6.6l2.2-2.2c.3-.3.7-.4 1-.2 1.1.4 2.3.6 3.6.6.6 0 1 .4 1 1V20c0 .6-.4 1-1 1A17 17 0 0 1 3 4c0-.6.4-1 1-1h3.5c.6 0 1 .4 1 1 0 1.3.2 2.5.6 3.6.1.3 0 .7-.2 1z"/></svg>
      </li>
      <li class="email">vora@halvocare.ca
        <svg viewBox="0 0 24 24"><rect x="1" y="4" width="22" height="16" fill="var(--blue)"/><path d="M2 5l10 8 10-8" stroke="#fff" stroke-width="2" fill="none"/></svg>
      </li>
    </ul>

    <div class="band">
      <svg viewBox="0 0 639 46" preserveAspectRatio="none">
        <polygon points="0,0 477,0 527,46 0,46" fill="var(--teal)"/>
        <polygon points="490,0 639,0 639,46 541,46" fill="var(--blue)"/>
      </svg>
      <div class="band-url">MEDICALVORA.CA</div>
    </div>
  </section>

</body>
</html>
```